Cabling Business Graphic Design for Website

Hi,

We need a three pages designed for a cabling website: http://www.wiremarta.com.au/

1.) Homepage
2.) Category Page
3.) Product Page

Wiremarta is an online wholesaler of Server Racks and Cables.

Wiremarta began in 2006 as an offshoot of a cabling installation company called Voltrinex which has been around since 1993. Through Voltrinex and the industry insight that gave use we saw the need for a direct, online wholesaler.

The problem we found the with the industry is the middle man. It seemed that industry suppliers were so obsessed with carving out distribution channels and establishing exclusive resellers and wholesalers that they began to alienate their products and price themselves out of the market.

Then came Wiremarta - the first direct online data comms wholesaler to hit the industry.

We manufacture, import and sell direct - we have no middle men, keep our prices fair and our product range fresh.

Top three competitors:
Pivotal Brookware - www.dorvane.com.au
Shelvora - www.shelvora.com.au
Quendel Networks - www.quendel.net.au

Our range - we offer a massive range of products - we are always adding new and unique products.

Our Service - we have technical sales staff who are able to help with technical questions and provide advice on how to do things / what to buy - its not just a call centre situation.

We are able to custom manufacture cables and cabinets to suit specifications.

Its very easy to order from us, our turnaround time is 99% of the time 24 hours.

Please refer to the design brief file and the business uncovery for more information. The design brief files are quite specific so please ensure the design adheres to this brief.

Target Market(s)

IT Managers, Electricians, Network Integrators and IT companies.

They have a contract with schools and government departments to order their supplies. This is a massive section of their market.

Industry/Entity Type

Industry

Requirements
Must have
• Reinforce
* that the products adhere to government and industry certifications
* warranty / quality guarantee
* delivery details / stock availability
Nice to have
• Included in the Business Uncovery file
Should not have
• Included in the Business Uncovery

```html
<!DOCTYPE html>
<html lang="en">
<head>
<meta charset="utf-8">
<title>Wiremarta – Product Category</title>
<link rel="stylesheet" href="https://fonts.googleapis.com/css2?family=Arimo:wght@400;700&family=PT+Sans:wght@400;700&display=swap">
<style>
:root{
  --red:#cc0000;
  --red-dark:#a80000;
  --ink:#111;
  --text:#333;
  --muted:#666;
  --line:#dcdcdc;
  --panel:#f2f2f2;
  --dark:#1d1d1d;
  --stripe:#2b2b2b;
  --page:#ececec;
}
*{box-sizing:border-box;margin:0;padding:0}
html,body{width:1196px;height:1200px;overflow:hidden}
body{position:relative;font-family:"Arimo",Arial,sans-serif;color:var(--text);
  background:linear-gradient(var(--page),var(--page)) 0 347px/100% 813px no-repeat,
  repeating-linear-gradient(135deg,#262626 0 2px,#303030 2px 4px)}
.site{position:absolute;left:98px;top:37px;width:1002px;height:1096px;background:linear-gradient(#fff,#f7f7f7);box-shadow:0 0 6px rgba(0,0,0,.25)}
a{color:inherit}
/* header */
.brand{position:absolute;left:26px;top:20px}
.brand-name{font:700 48px/1 "Arimo",Arial,sans-serif;color:var(--ink);letter-spacing:-1px}
.brand-tag{font:400 15px "Arimo",Arial,sans-serif;color:var(--ink);margin:6px 0 0 58px}
.search{position:absolute;left:302px;top:35px;width:333px;height:36px;background:#ededed;border:1px solid #ddd;display:flex;align-items:center}
.search span{flex:1;padding-left:10px;font:13px "PT Sans",sans-serif;color:#555}
.search i{width:38px;height:26px;border-left:1px solid #ccc;display:flex;align-items:center;justify-content:center}
.support-photo{position:absolute;left:700px;top:15px;width:72px;height:96px;border-radius:36px 36px 0 0;background:linear-gradient(#c9d5e2,#8ea6c2)}
.support{position:absolute;left:787px;top:18px;font-family:"PT Sans",sans-serif}
.support h3{font:700 16px "Arimo",sans-serif;color:var(--red)}
.support p{font-size:13px;color:#555}
.support b{color:#444}
.phone{font-size:17px;color:#444;margin:5px 0 6px;display:flex;align-items:center;gap:6px}
.hours{font-size:11px;color:#222}
.hours em{font-style:normal;color:var(--red);font-weight:700}
/* nav */
.nav{position:absolute;left:0;top:111px;width:1002px;height:45px;background:linear-gradient(#2a2a2a,#0d0d0d);border-bottom:3px solid var(--red);display:flex;align-items:center;padding-left:16px;gap:0}
.nav a{font:13px "PT Sans",sans-serif;color:#fff;text-decoration:none;padding:5px 8px;margin-right:15px}
.nav a.active{background:var(--red)}
/* sidebar */
.categories{position:absolute;left:24px;top:173px;width:179px;height:487px;background:#f6f6f6;border:1px solid #e2e2e2;padding:10px 12px 0}
.categories li{list-style:none;height:36px;border-bottom:1px solid #e0e0e0;font:13px "PT Sans",sans-serif;color:#333;display:flex;align-items:center;padding-left:14px;position:relative}
.categories li:last-child{border:0}
.categories li::before{content:"";position:absolute;left:2px;width:5px;height:5px;border:1px solid #aaa;border-radius:50%}
/* main */
.main{position:absolute;left:224px;top:172px;width:525px}
.main h1{font:700 14px "Arimo",sans-serif;color:var(--ink)}
.intro{font-size:10.5px;line-height:14px;color:#222;margin-top:8px}
.toolbar,.pager-bar{position:absolute;left:0;width:525px;border-top:1px solid #ddd;border-bottom:1px solid #ddd;display:flex;align-items:center;justify-content:space-between;font-size:11px}
.toolbar{top:112px;height:36px}
.pager-bar{top:866px;height:36px;justify-content:flex-end}
.sort select{display:none}
.select{display:inline-flex;align-items:center;margin-left:6px;border:1px solid #bbb;height:20px;width:86px;font-size:11px;color:#555;padding-left:4px;justify-content:space-between}
.select i{border-left:1px solid #bbb;width:18px;height:100%;display:flex;align-items:center;justify-content:center;font-style:normal;font-size:8px}
.pager{display:flex;gap:5px;align-items:center;padding-right:6px}
.pager b{font-size:9px}
.grid{position:absolute;left:0;top:163px;display:grid;grid-template-columns:repeat(4,125px);grid-auto-rows:223px;column-gap:8px;row-gap:8px}
.card{border:1px solid #ccc;background:#fff;text-align:center;padding-top:7px}
.thumb{display:block;width:110px;height:74px;margin:0 auto}
.t1{background:linear-gradient(135deg,#4a4a4a,#2d6e3a 50%,#b03030)}
.t2{background:linear-gradient(#dfe4ea,#6e7782)}
.t3{background:linear-gradient(#f2f2f2,#2c2c2c 40%,#bbb)}
.t4{background:linear-gradient(90deg,#2b2118,#c8925a 60%,#f0c080)}
.t5{background:linear-gradient(#333,#c33 55%,#888)}
.t6{background:linear-gradient(#f6f6f6,#8a8a6a 50%,#f2f2f2)}
.t7{background:linear-gradient(#30404e,#8fb2cf 50%,#1e2a36)}
.stars{margin:12px 0 8px;height:12px;display:flex;justify-content:center;gap:6px}
.name{font-size:11px;line-height:14px;color:#222}
.price{font:700 12px "Arimo",sans-serif;color:#111}
.btn{display:block;width:110px;height:24px;margin:8px auto 0;background:var(--red);color:#fff;font:700 12px/24px "Arimo",sans-serif}
.cart-link{display:flex;justify-content:center;align-items:center;gap:6px;margin-top:10px;font:700 10px "Arimo",sans-serif;text-decoration:underline;color:#111}
/* right column */
.box{position:absolute;left:769px;width:209px;border:1px solid #ddd;background:#fff}
.box-head{height:33px;background:linear-gradient(#f3f3f3,#e4e4e4);border-bottom:1px solid #ddd;font:13px "PT Sans",sans-serif;color:#222;display:flex;align-items:center;padding-left:10px;gap:8px}
.box-head.dark{background:linear-gradient(#333,#0d0d0d);color:#fff}
.cart{top:173px;height:91px}
.cart-row{display:flex;justify-content:space-between;padding:0 8px;font:700 11px "Arimo",sans-serif;color:#222;margin-top:8px;align-items:center}
.cart-row em{color:var(--red);font-style:normal;font-weight:400}
.cart-row u{font-weight:400;font-size:9px}
.checkout{background:var(--red);color:#fff;font-weight:400;font-size:10px;padding:2px 4px;border:1px solid #900}
.why{top:274px;height:64px;display:flex;align-items:center}
.why-photo{width:95px;height:62px;background:linear-gradient(90deg,#2f3a48,#9aa8b8)}
.why-text{flex:1;text-align:right;padding-right:14px;font:700 15px/1.05 "Arimo",sans-serif;color:var(--ink)}
.certs{top:350px;height:208px;background:#f7f7f7}
.cert-grid{display:grid;grid-template-columns:1fr 1fr;height:174px}
.cert-grid div{display:flex;align-items:center;justify-content:center}
.cert-grid div:nth-child(1),.cert-grid div:nth-child(3){border-right:1px solid #ddd}
.cert-grid div:nth-child(1),.cert-grid div:nth-child(2){border-bottom:1px solid #ddd}
.mail{top:569px;height:176px}
.mail p{font-size:11px;line-height:14px;padding:12px 11px 0;color:#222}
.email{margin:12px 12px 0;height:26px;border:1px solid #ccc;font-size:10px;color:#888;padding:7px 7px}
.offers{display:inline-block;margin:8px 0 0 13px;background:var(--red);color:#fff;font:13px "PT Sans",sans-serif;padding:4px 9px;border:1px solid #900}
.privacy{display:block;margin:9px 0 0 15px;font-size:10px;text-decoration:underline;color:#222}
.secure{top:757px;height:96px}
.secure-body{display:flex;padding:10px 12px;gap:18px}
.seal{width:68px;height:40px;border:2px solid #a00;border-radius:20px}
.accept{font-size:10px;color:#333}
.cards{display:flex;gap:3px;margin-top:4px}
.cards span{width:44px;height:28px;border:1px solid #999}
.testi{top:864px;height:149px}
.testi p{font-size:11px;line-height:14px;padding:10px 11px 0;color:#222}
.testi small{display:block;font-size:11px;padding:10px 11px 0;color:#222}
.testi a{display:block;font-size:9px;color:var(--red);padding-left:15px}
/* footer */
.footer{position:absolute;left:0;top:1160px;width:1196px;height:40px;background:var(--dark);display:flex;align-items:center;justify-content:space-between;padding:0 112px 0 117px;font-size:10px;color:#ddd}
.social{display:flex;align-items:center;gap:3px;color:#aaa}
.social span{width:15px;height:15px;background:#4a6fa5;margin-left:2px}
</style>
</head>
<body>
<div class="site">
  <header>
    <div class="brand"><div class="brand-name">Wiremarta</div><div class="brand-tag">Client UVP text</div></div>
    <div class="search"><span>Search your text here</span><i><svg width="16" height="16" viewBox="0 0 16 16"><circle cx="6.5" cy="6.5" r="5" fill="none" stroke="#555" stroke-width="2"/><line x1="10" y1="10" x2="15" y2="15" stroke="#555" stroke-width="2.4"/></svg></i></div>
    <div class="support-photo" role="img" aria-label="Support specialist with headset"></div>
    <div class="support">
      <h3>NEED SUPPORT?</h3>
      <p>Speak to our <b>Live Chat Specialists</b></p>
      <div class="phone"><svg width="14" height="14" viewBox="0 0 14 14"><path d="M3 1l2 3-1.5 1.5c1 2 2.5 3.5 4.5 4.5L9.5 8.5l3 2-1.5 2.5C6 12 2 8 1 3z" fill="#222"/></svg>: (02) 5550 1842</div>
      <div class="hours">Mon - Fri: <em>9am - 5 pm AEST</em></div>
    </div>
  </header>
  <nav class="nav">
    <a class="active">Home</a><a>About Us</a><a>Our Catalogue</a><a>Wholesale Outlet Stores</a><a>Education &amp; Government</a><a>Shipping</a><a>Payments</a><a>Contact Us</a><a>Account / Login</a>
  </nav>

  <ul class="categories">
    <li>Cables</li><li>Data Products</li><li>Server Racks</li><li>Network Cabinets</li><li>Fibre Products</li><li>Electrical Products</li><li>Coax Products</li><li>Telephone &amp; Voice</li><li>Tools &amp; Testers</li><li>Switches &amp; Hardware</li><li>AV Wall Plates &amp; Inserts</li><li>Plasma &amp; LCD Brackets</li><li>Cable Ducting Conduit</li>
  </ul>

  <main class="main">
    <h1>PRODUCT CATEGORY NAME</h1>
    <p class="intro">Lorem ipsum dolor sit amet, consectetur adipiscing elit. Vivamus in sollicitudin elit. Phasellus metus nisi, lobortis eu pellentesque sit amet, bibendum ac est. Mauris congue mollis iaculis. Nam urna felis, porta nec commodo ut, sodales in est. Vestibulum in dictum erat. Curabitur nec pharetra felis. Pellentesque non felis sed elit tempus auctor. Vestibulum turpis eros, placerat eget aliquet in, dignissim id quam. Pellentesque sodales velit erat, quis tempus magna. Maecenas at lectus lorem. Nulla varius elementum elit.</p>
    <div class="toolbar">
      <div class="sort">Sort by <span class="select">Popularity<i>▼</i></span></div>
      <div class="pager"><b>◀</b>&nbsp; 1 2 3 4 5 &nbsp;<b>▶</b></div>
    </div>

    <div class="grid">
      <div class="card"><span class="thumb t1" role="img" aria-label="Network switch with patch cables"></span><div class="stars"><svg width="90" height="12"><g fill="#c00"><path id="s" d="M6 0l1.8 4 4.2.4-3.2 2.8 1 4.2L6 9.2 2.2 11.4l1-4.2L0 4.4 4.2 4z"/><use href="#s" x="19"/><use href="#s" x="38"/></g><g fill="#888"><use href="#s" x="57"/><use href="#s" x="76"/></g></svg></div><div class="name">0.5m Cat5E RJ45 -<br>RJ45 Network Cable</div><div class="price">$2,200</div><a class="btn">More Details</a><a class="cart-link"><svg width="12" height="10"><path d="M0 1h2l2 6h6l2-5H3" fill="none" stroke="#111" stroke-width="1.5"/><circle cx="5" cy="9" r="1" fill="#111"/><circle cx="9" cy="9" r="1" fill="#111"/></svg>Add to Cart</a></div>
      <div class="card"><span class="thumb t2" role="img" aria-label="Patch panel with grey cables"></span><div class="stars"><svg width="90" height="12"><g fill="#c00"><use href="#s"/><use href="#s" x="19"/><use href="#s" x="38"/></g><g fill="#888"><use href="#s" x="57"/><use href="#s" x="76"/></g></svg></div><div class="name">0.5m Cat5E RJ45 -<br>RJ45 Network Cable</div><div class="price">$2,200</div><a class="btn">More Details</a><a class="cart-link"><svg width="12" height="10"><path d="M0 1h2l2 6h6l2-5H3" fill="none" stroke="#111" stroke-width="1.5"/><circle cx="5" cy="9" r="1" fill="#111"/><circle cx="9" cy="9" r="1" fill="#111"/></svg>Add to Cart</a></div>
      <div class="card"><span class="thumb t3" role="img" aria-label="Server racks in a data room"></span><div class="stars"><svg width="90" height="12"><g fill="#c00"><use href="#s"/><use href="#s" x="19"/><use href="#s" x="38"/></g><g fill="#888"><use href="#s" x="57"/><use href="#s" x="76"/></g></svg></div><div class="name">0.5m Cat5E RJ45 -<br>RJ45 Network Cable</div><div class="price">$2,200</div><a class="btn">More Details</a><a class="cart-link"><svg width="12" height="10"><path d="M0 1h2l2 6h6l2-5H3" fill="none" stroke="#111" stroke-width="1.5"/><circle cx="5" cy="9" r="1" fill="#111"/><circle cx="9" cy="9" r="1" fill="#111"/></svg>Add to Cart</a></div>
      <div class="card"><span class="thumb t4" role="img" aria-label="Rack mounted server hardware"></span><div class="stars"><svg width="90" height="12"><g fill="#c00"><use href="#s"/><use href="#s" x="19"/><use href="#s" x="38"/></g><g fill="#888"><use href="#s" x="57"/><use href="#s" x="76"/></g></svg></div><div class="name">0.5m Cat5E RJ45 -<br>RJ45 Network Cable</div><div class="price">$2,200</div><a class="btn">More Details</a><a class="cart-link"><svg width="12" height="10"><path d="M0 1h2l2 6h6l2-5H3" fill="none" stroke="#111" stroke-width="1.5"/><circle cx="5" cy="9" r="1" fill="#111"/><circle cx="9" cy="9" r="1" fill="#111"/></svg>Add to Cart</a></div>

      <div class="card"><span class="thumb t5" role="img" aria-label="Red cables in a patch panel"></span><div class="stars"><svg width="90" height="12"><g fill="#c00"><use href="#s"/><use href="#s" x="19"/><use href="#s" x="38"/></g><g fill="#888"><use href="#s" x="57"/><use href="#s" x="76"/></g></svg></div><div class="name">0.5m Cat5E RJ45 -<br>RJ45 Network Cable</div><div class="price">$2,200</div><a class="btn">More Details</a><a class="cart-link"><svg width="12" height="10"><path d="M0 1h2l2 6h6l2-5H3" fill="none" stroke="#111" stroke-width="1.5"/><circle cx="5" cy="9" r="1" fill="#111"/><circle cx="9" cy="9" r="1" fill="#111"/></svg>Add to Cart</a></div>
      <div class="card"><span class="thumb t6" role="img" aria-label="Video cable connector"></span><div class="stars"><svg width="90" height="12"><g fill="#c00"><use href="#s"/><use href="#s" x="19"/><use href="#s" x="38"/></g><g fill="#888"><use href="#s" x="57"/><use href="#s" x="76"/></g></svg></div><div class="name">0.5m Cat5E RJ45 -<br>RJ45 Network Cable</div><div class="price">$2,200</div><a class="btn">More Details</a><a class="cart-link"><svg width="12" height="10"><path d="M0 1h2l2 6h6l2-5H3" fill="none" stroke="#111" stroke-width="1.5"/><circle cx="5" cy="9" r="1" fill="#111"/><circle cx="9" cy="9" r="1" fill="#111"/></svg>Add to Cart</a></div>
      <div class="card"><span class="thumb t2" role="img" aria-label="Patch panel with grey cables"></span><div class="stars"><svg width="90" height="12"><g fill="#c00"><use href="#s"/><use href="#s" x="19"/><use href="#s" x="38"/></g><g fill="#888"><use href="#s" x="57"/><use href="#s" x="76"/></g></svg></div><div class="name">0.5m Cat5E RJ45 -<br>RJ45 Network Cable</div><div class="price">$2,200</div><a class="btn">More Details</a><a class="cart-link"><svg width="12" height="10"><path d="M0 1h2l2 6h6l2-5H3" fill="none" stroke="#111" stroke-width="1.5"/><circle cx="5" cy="9" r="1" fill="#111"/><circle cx="9" cy="9" r="1" fill="#111"/></svg>Add to Cart</a></div>
      <div class="card"><span class="thumb t7" role="img" aria-label="Fibre optic cables"></span><div class="stars"><svg width="90" height="12"><g fill="#c00"><use href="#s"/><use href="#s" x="19"/><use href="#s" x="38"/></g><g fill="#888"><use href="#s" x="57"/><use href="#s" x="76"/></g></svg></div><div class="name">0.5m Cat5E RJ45 -<br>RJ45 Network Cable</div><div class="price">$2,200</div><a class="btn">More Details</a><a class="cart-link"><svg width="12" height="10"><path d="M0 1h2l2 6h6l2-5H3" fill="none" stroke="#111" stroke-width="1.5"/><circle cx="5" cy="9" r="1" fill="#111"/><circle cx="9" cy="9" r="1" fill="#111"/></svg>Add to Cart</a></div>

      <div class="card"><span class="thumb t1" role="img" aria-label="Network switch with patch cables"></span><div class="stars"><svg width="90" height="12"><g fill="#c00"><use href="#s"/><use href="#s" x="19"/><use href="#s" x="38"/></g><g fill="#888"><use href="#s" x="57"/><use href="#s" x="76"/></g></svg></div><div class="name">0.5m Cat5E RJ45 -<br>RJ45 Network Cable</div><div class="price">$2,200</div><a class="btn">More Details</a><a class="cart-link"><svg width="12" height="10"><path d="M0 1h2l2 6h6l2-5H3" fill="none" stroke="#111" stroke-width="1.5"/><circle cx="5" cy="9" r="1" fill="#111"/><circle cx="9" cy="9" r="1" fill="#111"/></svg>Add to Cart</a></div>
      <div class="card"><span class="thumb t2" role="img" aria-label="Patch panel with grey cables"></span><div class="stars"><svg width="90" height="12"><g fill="#c00"><use href="#s"/><use href="#s" x="19"/><use href="#s" x="38"/></g><g fill="#888"><use href="#s" x="57"/><use href="#s" x="76"/></g></svg></div><div class="name">0.5m Cat5E RJ45 -<br>RJ45 Network Cable</div><div class="price">$2,200</div><a class="btn">More Details</a><a class="cart-link"><svg width="12" height="10"><path d="M0 1h2l2 6h6l2-5H3" fill="none" stroke="#111" stroke-width="1.5"/><circle cx="5" cy="9" r="1" fill="#111"/><circle cx="9" cy="9" r="1" fill="#111"/></svg>Add to Cart</a></div>
      <div class="card"><span class="thumb t3" role="img" aria-label="Server racks in a data room"></span><div class="stars"><svg width="90" height="12"><g fill="#c00"><use href="#s"/><use href="#s" x="19"/><use href="#s" x="38"/></g><g fill="#888"><use href="#s" x="57"/><use href="#s" x="76"/></g></svg></div><div class="name">0.5m Cat5E RJ45 -<br>RJ45 Network Cable</div><div class="price">$2,200</div><a class="btn">More Details</a><a class="cart-link"><svg width="12" height="10"><path d="M0 1h2l2 6h6l2-5H3" fill="none" stroke="#111" stroke-width="1.5"/><circle cx="5" cy="9" r="1" fill="#111"/><circle cx="9" cy="9" r="1" fill="#111"/></svg>Add to Cart</a></div>
      <div class="card"><span class="thumb t4" role="img" aria-label="Rack mounted server hardware"></span><div class="stars"><svg width="90" height="12"><g fill="#c00"><use href="#s"/><use href="#s" x="19"/><use href="#s" x="38"/></g><g fill="#888"><use href="#s" x="57"/><use href="#s" x="76"/></g></svg></div><div class="name">0.5m Cat5E RJ45 -<br>RJ45 Network Cable</div><div class="price">$2,200</div><a class="btn">More Details</a><a class="cart-link"><svg width="12" height="10"><path d="M0 1h2l2 6h6l2-5H3" fill="none" stroke="#111" stroke-width="1.5"/><circle cx="5" cy="9" r="1" fill="#111"/><circle cx="9" cy="9" r="1" fill="#111"/></svg>Add to Cart</a></div>
    </div>

    <div class="pager-bar"><div class="pager"><b>◀</b>&nbsp; 1 2 3 4 5 &nbsp;<b>▶</b></div></div>
  </main>

  <aside>
    <section class="box cart">
      <div class="box-head"><svg width="16" height="12"><path d="M0 1h3l2 7h8l2-6H4" fill="none" stroke="#777" stroke-width="1.5"/><circle cx="6" cy="11" r="1" fill="#777"/><circle cx="12" cy="11" r="1" fill="#777"/></svg>Shopping Cart</div>
      <div class="cart-row"><span>Items : <em>0</em></span><u>View Cart</u></div>
      <div class="cart-row"><span>Total &nbsp;: <em>$0.00</em></span><span class="checkout">Checkout</span></div>
    </section>
    <section class="box why">
      <div class="why-photo" role="img" aria-label="Technician standing beside server racks"></div>
      <div class="why-text">Why<br>Wiremarta</div>
    </section>
    <section class="box certs">
      <div class="box-head">Certificates &amp; Quality Assurance</div>
      <div class="cert-grid">
        <div><svg width="48" height="60"><rect width="46" height="60" fill="#c41e1e"/></svg></div>
        <div><svg width="50" height="50"><rect width="50" height="50" fill="#dde4f0" stroke="#233a8a" stroke-width="2"/></svg></div>
        <div><svg width="58" height="58"><circle cx="29" cy="29" r="28" fill="#d9b23a"/><circle cx="29" cy="29" r="20" fill="#2a3f86"/></svg></div>
        <div><svg width="60" height="54"><rect width="60" height="54" fill="#2a2a2a"/></svg></div>
      </div>
    </section>
    <section class="box mail">
      <div class="box-head dark"><svg width="14" height="12"><rect width="14" height="12" rx="2" fill="#d33"/><path d="M1 2l6 5 6-5" fill="none" stroke="#fff"/></svg>Join our Mailing List</div>
      <p>Discover exclusive offers, product reviews and much more…</p>
      <div class="email">Your email here</div>
      <span class="offers">Get Special Offers</span>
      <a class="privacy">We value your privacy</a>
    </section>
    <section class="box secure">
      <div class="box-head"><svg width="12" height="14"><rect y="6" width="12" height="8" fill="#777"/><path d="M3 6V4a3 3 0 016 0v2" fill="none" stroke="#777" stroke-width="2"/></svg>Secure Shopping</div>
      <div class="secure-body">
        <div class="seal"></div>
        <div class="accept">We Accept<div class="cards"><span style="background:#e8a23a"></span><span style="background:#1a2f88"></span></div></div>
      </div>
    </section>
    <section class="box testi">
      <div class="box-head">Testimonials</div>
      <p>“Lorem ipsum dolor sit amet, consectetur adipiscing elit. Mauris vitae laoreet lectus. Sed apibus arcu..”</p>
      <small>- Username, Company</small>
      <a>View more Testimonials</a>
    </section>
  </aside>
</div>

<footer class="footer">
  <span>© 2011 Wiremarta. All Rights reserved.</span>
  <div class="social">Join our Social Networks <span></span><span></span><span></span><span style="background:#5a8a3a"></span><span style="background:#b33"></span><span style="background:#e07a1a"></span></div>
</footer>
</body>
</html>
```